Commercial janitorial cleaning

Janitorial cleaning particularly for commercial buildings. Website needs to specify free estimates. Location of service is Hudson, Valatie, East Greenbush, Troy, Albany ny area. Services page with Janitorial services- General Office Cleaning, Construction Cleaning, Carpet Extraction, Consultation/Business, Lighting Maintenance, Seasonal Deep Cleaning, Window cleaning, Event Cleaning, Floor and Carpet Cleaning, Floor Striping and Waxing. Contact us page with email phone number on page and a request page that emails me if they have any questions. About us page-the picture of my family on it with a section I can type a story myself.

Target Market(s)

Commercial businesses

Industry/Entity Type

Janitorial Service

Number of Pages Required

4 page

Font styles to use
Serif
Sans Serif
Script

Colors
ec1f27
1b1b1b
ffffff
9d9d9d

Requirements
Must have
• Phone number 555-304-7162. Must have free estimates on home page. Going for industrial / modern look to website
Nice to have
• Logo is a red and black building so if those colors could be coordinated to website that would be awesome.

```html
<!DOCTYPE html>
<html lang="en">
<head>
<meta charset="utf-8">
<title>Brightline Cleaning Services</title>
<link href="https://fonts.googleapis.com/css2?family=Roboto:wght@400;500;700&family=Lato:wght@400;700&family=Raleway:wght@600;700&display=swap" rel="stylesheet">
<style>
:root{
  --red:#ec1f27;
  --ink:#1b1b1b;
  --white:#ffffff;
  --grey:#9d9d9d;
  --soft:#f4f4f4;
  --body:#444444;
}
*{box-sizing:border-box;margin:0;padding:0}
html,body{width:668px;height:1200px;overflow:hidden;background:var(--white)}
body{position:relative;font-family:'Lato',sans-serif;color:var(--ink)}
.abs{position:absolute}

/* header */
.site-header{position:absolute;left:0;top:0;width:668px;height:64px;background:var(--white)}
.brand{position:absolute;left:44px;top:10px;display:flex;align-items:center;gap:8px}
.brand-mark{width:36px;height:36px;background:var(--red)}
.brand-name{font-family:'Roboto',sans-serif;font-weight:700;font-size:15px;line-height:16px;color:var(--ink)}
.cta{position:absolute;display:flex;align-items:center;justify-content:center;background:var(--red);color:var(--white);font-family:'Roboto',sans-serif;font-weight:500;font-size:10px;border:1px solid var(--ink);box-shadow:2px 2px 0 var(--ink)}
.cta-top{left:430px;top:7px;width:95px;height:20px}
.phone{position:absolute;left:537px;top:11px;display:flex;align-items:center;gap:6px;font-family:'Roboto',sans-serif;font-weight:500;font-size:10.5px;color:var(--ink)}
.main-nav{position:absolute;top:40px;left:0;width:668px;height:14px}
.main-nav a{position:absolute;top:0;transform:translateX(-50%);font-family:'Roboto',sans-serif;font-weight:500;font-size:9px;color:var(--ink);text-decoration:none;white-space:nowrap}
.main-nav a.active{color:var(--red)}
.main-nav a.active::after{content:"";position:absolute;left:-6px;right:-6px;top:15px;height:2px;background:var(--red)}
.nav-sep{position:absolute;top:42px;width:1px;height:8px;background:#d0d0d0}

/* hero */
.hero{position:absolute;left:0;top:64px;width:668px;height:269px;background:linear-gradient(160deg,#3d6fb0 0%,#6f98cc 35%,#c0313a 60%,#8a1f25 80%,#3a3a3a 100%)}
.hero-band{position:absolute;left:0;bottom:0;width:100%;height:49px;background:rgba(20,20,20,.55);text-align:center;color:var(--white);font-family:'Raleway',sans-serif}
.hero-title{font-weight:700;font-size:16px;margin-top:7px}
.hero-sub{font-weight:600;font-size:11px;margin-top:3px}
.hero-arrow{position:absolute;top:300px}

/* section heading */
.sec-title{position:absolute;left:0;width:668px;text-align:center;font-family:'Roboto',sans-serif;font-weight:500;color:var(--ink)}
.sec-title em{font-style:normal;color:var(--red)}
.rule{position:absolute;height:1px;background:#bdbdbd}
.rule::after{content:"";position:absolute;left:50%;top:-1px;width:22px;height:3px;margin-left:-11px;background:var(--red)}

/* services */
.service{position:absolute;width:110px}
.service svg{display:block}
.service-art{position:absolute;left:22px;top:18px;width:30px;height:30px;background:var(--ink)}
.service.active .service-art{background:var(--white)}
.service-name{position:absolute;left:0;top:78px;font-family:'Roboto',sans-serif;font-size:11px;line-height:15px;color:#333}
.service.active .service-name{color:var(--red);font-weight:500}

/* about */
.about{position:absolute;left:0;top:706px;width:668px;height:194px;background:var(--soft)}
.copy{position:absolute;left:52px;width:564px;text-align:center;font-size:7.6px;line-height:12.8px;color:var(--body)}
.btn-more{position:absolute;left:285px;top:849px;width:98px;height:27px;border:1px solid var(--red);background:var(--white);color:var(--red);font-family:'Roboto',sans-serif;font-weight:500;font-size:9.5px;display:flex;align-items:center;justify-content:center;gap:5px;clip-path:polygon(6px 0,100% 0,100% calc(100% - 6px),calc(100% - 6px) 100%,0 100%,0 6px)}

/* testimonials */
.avatar{position:absolute;left:307px;top:987px;width:54px;height:54px;border-radius:50%;border:2px solid var(--red);padding:3px;background:var(--white)}
.avatar span{display:block;width:100%;height:100%;border-radius:50%;background:linear-gradient(#c9b6a6,#8a7a70)}
.client{position:absolute;left:0;top:1046px;width:668px;text-align:center;font-size:7.5px;font-weight:700;color:var(--red)}
.quote{position:absolute;left:68px;top:1071px;width:532px;text-align:center;font-size:7.4px;line-height:12.8px;color:var(--body)}
.qmark{position:absolute;font-family:Georgia,serif;font-size:28px;color:#c8c8c8}
.dots{position:absolute;top:1127px;left:323px;display:flex;gap:3px}
.dots i{width:5px;height:5px;border-radius:50%;background:var(--grey)}
.dots i.on{background:var(--red)}

/* footer */
.site-footer{position:absolute;left:0;top:1158px;width:668px;height:42px;background:var(--ink);color:var(--white)}
.foot-nav{position:absolute;left:44px;top:11px;display:flex;font-size:7px}
.foot-nav a{color:var(--white);text-decoration:none;padding:0 7px;border-left:1px solid #666}
.foot-nav a:first-child{padding-left:0;border-left:0}
.legal{position:absolute;left:44px;top:25px;font-size:7px;color:#ddd}
.cta-foot{left:368px;top:12px;width:96px;height:20px;border-color:var(--white);box-shadow:none}
.social{position:absolute;left:541px;top:13px;display:flex;gap:4px}
.social span{width:17px;height:17px;border-radius:50%;border:1.2px solid var(--white)}
</style>
</head>
<body>

<header class="site-header">
  <div class="brand">
    <div class="brand-mark"></div>
    <div class="brand-name">Brightline<br>Cleaning Services</div>
  </div>
  <div class="cta cta-top">Free Estimates</div>
  <div class="phone">
    <svg width="15" height="15" viewBox="0 0 16 16" aria-hidden="true"><circle cx="8" cy="8" r="7" fill="none" stroke="#ec1f27" stroke-width="1.2"/><path d="M5.5 4.5l1.5 0 .6 2-1 .8a5 5 0 0 0 2.1 2.1l.8-1 2 .6 0 1.5c-3.6.3-6.3-2.4-6-6z" fill="#ec1f27"/></svg>
    555-304-7162
  </div>
  <nav class="main-nav">
    <a class="active" style="left:356px">Home</a>
    <a style="left:434px">About Us</a>
    <a style="left:516px">Services</a>
    <a style="left:602px">Contact Us</a>
  </nav>
  <span class="nav-sep" style="left:395px"></span>
  <span class="nav-sep" style="left:478px"></span>
  <span class="nav-sep" style="left:558px"></span>
</header>

<section class="hero" role="img" aria-label="Photo of a modern red-striped commercial office tower against a blue sky">
  <div class="hero-band">
    <p class="hero-title">We Offer Janitorial Cleaning Particularly For Commercial Buildings</p>
    <p class="hero-sub">Serving All of Hudson, Valatie, Troy &amp; Albany</p>
  </div>
</section>
<svg class="hero-arrow" style="left:16px" width="10" height="14" viewBox="0 0 10 14" aria-hidden="true"><path d="M8 1L2 7l6 6" fill="none" stroke="#ffffff" stroke-opacity=".7" stroke-width="1.5"/></svg>
<svg class="hero-arrow" style="left:636px" width="10" height="14" viewBox="0 0 10 14" aria-hidden="true"><path d="M2 1l6 6-6 6" fill="none" stroke="#ffffff" stroke-opacity=".7" stroke-width="1.5"/></svg>

<h2 class="sec-title" style="top:364px;font-size:21px">Our <em>Services</em></h2>
<div class="rule" style="left:263px;top:405px;width:141px"></div>

<div class="service active" style="left:56px;top:442px">
  <svg width="76" height="68" viewBox="0 0 76 68" aria-hidden="true"><polygon points="13,1 75,1 75,55 62,67 1,67 1,13" fill="#1b1b1b"/><polygon points="14,4 72,4 72,54 61,64 4,64 4,14" fill="#ec1f27"/></svg>
  <div class="service-art" role="img" aria-label="Icon of a cleaner wiping a window"></div>
  <p class="service-name">General Office<br>Cleaning</p>
</div>
<div class="service" style="left:176px;top:442px">
  <svg width="76" height="68" viewBox="0 0 76 68" aria-hidden="true"><polygon points="13,1.5 74.5,1.5 74.5,55 62,66.5 1.5,66.5 1.5,13" fill="#fff" stroke="#ec1f27" stroke-width="1.6"/></svg>
  <div class="service-art" role="img" aria-label="Icon of a worker on a rope"></div>
  <p class="service-name">Construction<br>Cleaning</p>
</div>
<div class="service" style="left:296px;top:442px">
  <svg width="76" height="68" viewBox="0 0 76 68" aria-hidden="true"><polygon points="13,1.5 74.5,1.5 74.5,55 62,66.5 1.5,66.5 1.5,13" fill="#fff" stroke="#ec1f27" stroke-width="1.6"/></svg>
  <div class="service-art" role="img" aria-label="Icon of a worker vacuuming carpet"></div>
  <p class="service-name">Carpet<br>Extraction</p>
</div>
<div class="service" style="left:415px;top:442px">
  <svg width="76" height="68" viewBox="0 0 76 68" aria-hidden="true"><polygon points="13,1.5 74.5,1.5 74.5,55 62,66.5 1.5,66.5 1.5,13" fill="#fff" stroke="#ec1f27" stroke-width="1.6"/></svg>
  <div class="service-art" role="img" aria-label="Icon of a building with a person"></div>
  <p class="service-name">Consultation/<br>Business</p>
</div>
<div class="service" style="left:535px;top:442px">
  <svg width="76" height="68" viewBox="0 0 76 68" aria-hidden="true"><polygon points="13,1.5 74.5,1.5 74.5,55 62,66.5 1.5,66.5 1.5,13" fill="#fff" stroke="#ec1f27" stroke-width="1.6"/></svg>
  <div class="service-art" role="img" aria-label="Icon of an electrician with a screwdriver"></div>
  <p class="service-name">Lighting<br>Maintenance</p>
</div>

<div class="service" style="left:56px;top:574px">
  <svg width="76" height="68" viewBox="0 0 76 68" aria-hidden="true"><polygon points="13,1.5 74.5,1.5 74.5,55 62,66.5 1.5,66.5 1.5,13" fill="#fff" stroke="#ec1f27" stroke-width="1.6"/></svg>
  <div class="service-art" role="img" aria-label="Icon of a worker with a floor machine"></div>
  <p class="service-name">Seasonal Deep<br>Cleaning</p>
</div>
<div class="service" style="left:176px;top:574px">
  <svg width="76" height="68" viewBox="0 0 76 68" aria-hidden="true"><polygon points="13,1.5 74.5,1.5 74.5,55 62,66.5 1.5,66.5 1.5,13" fill="#fff" stroke="#ec1f27" stroke-width="1.6"/></svg>
  <div class="service-art" role="img" aria-label="Icon of a person wiping a window"></div>
  <p class="service-name">Window<br>cleaning</p>
</div>
<div class="service" style="left:296px;top:574px">
  <svg width="76" height="68" viewBox="0 0 76 68" aria-hidden="true"><polygon points="13,1.5 74.5,1.5 74.5,55 62,66.5 1.5,66.5 1.5,13" fill="#fff" stroke="#ec1f27" stroke-width="1.6"/></svg>
  <div class="service-art" role="img" aria-label="Icon of people at an outdoor table with umbrella"></div>
  <p class="service-name">Event<br>Cleaning</p>
</div>
<div class="service" style="left:415px;top:574px">
  <svg width="76" height="68" viewBox="0 0 76 68" aria-hidden="true"><polygon points="13,1.5 74.5,1.5 74.5,55 62,66.5 1.5,66.5 1.5,13" fill="#fff" stroke="#ec1f27" stroke-width="1.6"/></svg>
  <div class="service-art" role="img" aria-label="Icon of a person vacuuming the floor"></div>
  <p class="service-name">Floor and<br>Carpet Cleaning</p>
</div>
<div class="service" style="left:535px;top:574px">
  <svg width="76" height="68" viewBox="0 0 76 68" aria-hidden="true"><polygon points="13,1.5 74.5,1.5 74.5,55 62,66.5 1.5,66.5 1.5,13" fill="#fff" stroke="#ec1f27" stroke-width="1.6"/></svg>
  <div class="service-art" role="img" aria-label="Icon of a worker polishing a floor"></div>
  <p class="service-name">Floor Striping<br>and Waxing</p>
</div>

<section class="about"></section>
<h2 class="sec-title" style="top:731px;font-size:18px">About <em>Brightline Cleaning Services</em></h2>
<div class="rule" style="left:174px;top:769px;width:320px"></div>
<p class="copy" style="top:784px">Lorem ipsum dolor sit amet, consectetuer adipiscing elit, sed diam nonummy nibh euismod tincidunt ut laoreet dolore magna aliquam erat volutpat. Ut wisi enim ad minim veniam, quis nostrud exerci tation ullamcorper suscipit lobortis nisl ut aliquip ex ea commodo consequat. Duis autem vel eum iriure dolor in hendrerit in vulputate velit esse molestie consequat, vel illum dolore eu feugiat nulla facilisis at vero eros et accumsan et iusto odio dignissim qui blandit praesent luptatum zzril delenit augue duis dolore te feugait nulla facilisi.</p>
<div class="btn-more">Read More <svg width="6" height="7" viewBox="0 0 6 7" aria-hidden="true"><path d="M0 0l6 3.5L0 7z" fill="#1b1b1b"/></svg></div>

<h2 class="sec-title" style="top:922px;font-size:18px">Clients <em>Testimonials</em></h2>
<div class="rule" style="left:232px;top:961px;width:203px"></div>
<div class="avatar"><span role="img" aria-label="Portrait photo of the client"></span></div>
<p class="client">- Mark Delaney</p>
<span class="qmark" style="left:50px;top:1062px">&ldquo;</span>
<p class="quote">Lorem ipsum dolor sit amet, consectetuer adipiscing elit, sed diam nonummy nibh euismod tincidunt ut laoreet dolore magna aliquam erat volutpat. Ut wisi enim ad minim veniam, quis nostrud exerci tation ullamcorper suscipit lobortis nisl ut aliquip ex ea commodo consequat. Duis autem vel eum iriure dolor in hendrerit in vulputate velit esse molestie consequat, vel illum dolore eu feugiat nulla facilisis at.</p>
<span class="qmark" style="left:500px;top:1086px">&rdquo;</span>
<div class="dots"><i class="on"></i><i></i><i></i></div>

<footer class="site-footer">
  <nav class="foot-nav"><a>Home</a><a>About Us</a><a>Services</a><a>Contact Us</a></nav>
  <p class="legal">Copyright © 2017 Brightline Cleaning Services. All Right Reserved.</p>
  <div class="cta cta-foot">Free Estimates</div>
  <div class="social" aria-label="Social links"><span></span><span></span><span></span><span></span></div>
</footer>

</body>
</html>
```